Lorna Tess Tresses Fancy Business Card’s

I want my business cards to be elite, original and very classy. I want the business cards to match the colors of my logo and to match the design posted. I would love the design of the picture I posted

I want the card all white .
The dripping on the top of the card I want it to match the pink color in my logo that’s also posted .
I need my logo on the business card !
I need my Instagram- @lorna.tess.tresses__
And my phone number - 582 907 3365

Target Market(s)

My target market is young woman age 23 to older woman to the age of 65
I want both older and younger women to love my design . I don’t want any cheap looking business cards

Industry/Entity Type

Hair And Beauty

Contact Information for Business Card

Add my logo
Add my Instagram- @lorna.tess.tresses__
My number - 582 907 3365
My website- www.lornatesstresses.example

Font styles to use
Serif
Script

Colors
ffffff
e667a6
e34298

Requirements
Must have
• The business cards must have my logo, my number , my website, and my Instagram!
Nice to have
• Nice to have glitter words that match my logo
• The business cards must look classy and mature
• I want them to be very unique!!
Should not have
• Should not have any colors that doesn’t match my logo ! This is very important! Please

```html
<!DOCTYPE html>
<html lang="en">
<head>
<meta charset="utf-8">
<title>Lorna Tess Tresses – Business Cards</title>
<link rel="stylesheet" href="https://fonts.googleapis.com/css2?family=Playfair+Display:wght@600&family=Roboto:wght@400;500&display=swap">
<style>
  :root {
    --page-bg: #2a2c30;
    --card-white: #ffffff;
    --pink-light: #e667a6;
    --pink-deep: #e34298;
    --decor-grey: #e4e5e8;
    --text-white: #ffffff;
  }
  * { box-sizing: border-box; margin: 0; padding: 0; }
  html, body {
    width: 1200px; height: 900px; overflow: hidden;
    background: var(--page-bg);
  }
  .canvas {
    position: relative; width: 1200px; height: 900px;
    display: flex; flex-direction: column; align-items: center; justify-content: center; gap: 48px;
  }
  .card {
    position: relative; width: 700px; height: 400px;
    background: var(--card-white); overflow: hidden; border-radius: 4px;
    box-shadow: 0 10px 30px rgba(0,0,0,.35);
  }
  .band {
    position: absolute;
    background: linear-gradient(90deg, var(--pink-light), var(--pink-deep));
  }
  .band--top { top: 0; right: 0; width: 56%; height: 30px; border-radius: 0 0 0 30px; }
  .band--bottom { bottom: 0; left: 0; width: 52%; height: 30px; border-radius: 0 30px 0 0; }
  .decor {
    position: absolute; width: 150px; height: 120px;
    background: radial-gradient(ellipse at center, var(--decor-grey) 0%, rgba(228,229,232,0.35) 60%, rgba(255,255,255,0) 75%);
  }
  .decor--top-left { top: 20px; left: 24px; }
  .decor--bottom-right { bottom: 34px; right: 30px; }
  .brand {
    position: absolute; left: 0; right: 0;
    text-align: center;
    font-family: "Playfair Display", Georgia, serif; font-weight: 600;
    color: var(--pink-deep); font-size: 44px; line-height: 1.1; letter-spacing: 1px;
  }
  .card--front .brand { top: 122px; }
  .card--back .brand { top: 48px; font-size: 36px; }
  .contact-panel {
    position: absolute; left: 84px; top: 176px; width: 340px; height: 190px;
    border-radius: 22px;
    background: linear-gradient(160deg, var(--pink-light), var(--pink-deep));
    padding: 34px 30px; display: flex; flex-direction: column; gap: 14px;
  }
  .contact-line {
    display: flex; align-items: center; gap: 12px;
    font-family: "Roboto", Arial, sans-serif; font-weight: 500;
    font-size: 19px; color: var(--text-white);
  }
  .contact-icon { width: 18px; height: 18px; flex: none; }
</style>
</head>
<body>
<main class="canvas">
  <section class="card card--front" aria-label="Business card front">
    <div class="band band--top"></div>
    <div class="band band--bottom"></div>
    <div class="decor decor--top-left" role="img" aria-label="Faint scissors and hair strands decoration"></div>
    <div class="decor decor--bottom-right" role="img" aria-label="Faint scissors and hair strands decoration"></div>
    <h1 class="brand">Lorna Tess<br>Tresses</h1>
  </section>

  <section class="card card--back" aria-label="Business card back">
    <div class="band band--top"></div>
    <div class="decor decor--top-left" role="img" aria-label="Faint scissors and hair strands decoration"></div>
    <div class="decor decor--bottom-right" role="img" aria-label="Faint scissors and hair strands decoration"></div>
    <h2 class="brand">Lorna Tess<br>Tresses</h2>
    <div class="contact-panel">
      <p class="contact-line">
        <svg class="contact-icon" viewBox="0 0 24 24" aria-hidden="true"><path fill="#fff" d="M6.6 10.8a15.1 15.1 0 0 0 6.6 6.6l2.2-2.2c.3-.3.7-.4 1-.2 1.1.4 2.3.6 3.6.6.6 0 1 .4 1 1V20c0 .6-.4 1-1 1A17 17 0 0 1 3 4c0-.6.4-1 1-1h3.5c.6 0 1 .4 1 1 0 1.3.2 2.5.6 3.6.1.3 0 .7-.2 1z"/></svg>
        582 907 3365
      </p>
      <p class="contact-line">
        <svg class="contact-icon" viewBox="0 0 24 24" aria-hidden="true"><circle cx="12" cy="12" r="9" fill="none" stroke="#fff" stroke-width="2"/></svg>
        @lorna.tess.tresses__
      </p>
      <p class="contact-line">
        <svg class="contact-icon" viewBox="0 0 24 24" aria-hidden="true"><circle cx="12" cy="12" r="9" fill="none" stroke="#fff" stroke-width="2"/><path d="M3 12h18M12 3c3 3 3 15 0 18M12 3c-3 3-3 15 0 18" fill="none" stroke="#fff" stroke-width="1.6"/></svg>
        www.lornatesstresses.example
      </p>
    </div>
  </section>
</main>
</body>
</html>
```